Business card website / business card for website

We are a French website selling products Made in USA of quality, we need a business card to give from hand to hand and for deposit in the cartons of Each order. We-have the logo That I send in the attachments The theme is: US Vintage and find the compromised entre les national park ambience us and the atmosphere Brooklyn If you can make the feeling it's great The site www.latablederivebleue.com (opening April) You can change the logo a little gold in color it could ... we are a French website selling products Made in USA quality, we need a business card to give from hand to hand and deposit in cartons each order. we have the logo that I convey in the attached parts is the theme: Vintage embiance US and find a compromise between the atmosphere us national park and the atmosphere Brooklyn at: www.latablederivebleue.com (opening April) if you can the impression is great

Target Market(s)

25-50 YEARS man, woman.

Industry/Entity Type

Business

Contact Information for Business Card

www.latablederivebleue.com
N'oubliez pas que nous sommes là si vous avez besoin de nouscontact@latablederivebleue.com

Font styles to use
Serif

Requirements
Must have
• my logo with "general store", my email address preceded by the phrase: Do not forget that we are here if you need us My logo with the words "general store," my email address Preceded by the sentence: remember we're here if you need us (in french)
Nice to have
• i like this style: http://designcorbel.net/ideas/print-ideas/25-charming-old-style-business-card-designs/ must feel the Vintage America it must feel the Vintage America lice can change a little logo or to color ... You can change the logo a little gold in color it could ... i like kraft paper with red ....
Should not have

```html
<!DOCTYPE html>
<html lang="fr">
<head>
<meta charset="utf-8">
<title>Carte de visite — La Table de Rive Bleue</title>
<link rel="stylesheet" href="https://fonts.googleapis.com/css2?family=Courier+Prime:wght@400;700&display=swap">
<style>
  :root {
    --backdrop: #e4e2dd;
    --kraft: #d9cea3;
    --kraft-dark: #c9bb88;
    --ink: #25264f;
    --stamp: rgba(110, 100, 80, 0.16);
  }
  html, body {
    margin: 0;
    width: 1200px;
    height: 843px;
    overflow: hidden;
    background: var(--backdrop);
  }
  .card {
    position: absolute;
    left: 80px;
    top: 125px;
    width: 1040px;
    height: 594px;
    background: radial-gradient(ellipse at 40% 40%, var(--kraft) 55%, var(--kraft-dark) 100%);
    box-shadow: 0 10px 30px rgba(0,0,0,0.18);
    font-family: "Courier Prime", "Courier New", monospace;
    color: var(--ink);
  }
  .card-frame {
    position: absolute;
    inset: 0;
  }
  .postmark {
    position: absolute;
    left: 770px;
    top: 300px;
    width: 190px;
    height: 190px;
    border-radius: 50%;
    background: var(--stamp);
  }
  .brand-seal {
    position: absolute;
    left: 130px;
    top: 85px;
    width: 320px;
    height: 320px;
    border: 5px solid var(--ink);
    border-radius: 50%;
    box-sizing: border-box;
    display: flex;
    align-items: center;
    justify-content: center;
    text-align: center;
  }
  .brand-name {
    font-weight: 700;
    font-size: 32px;
    line-height: 1.2;
    letter-spacing: 1px;
    text-transform: uppercase;
    margin: 0;
    padding: 0 30px;
  }
  .reminder {
    position: absolute;
    left: 510px;
    top: 110px;
    margin: 0;
    font-weight: 700;
    font-size: 40px;
    line-height: 1.12;
    letter-spacing: 0.5px;
  }
  .reminder .initial {
    font-size: 58px;
    line-height: 1;
  }
  .contact {
    position: absolute;
    left: 0;
    right: 0;
    margin: 0;
    text-align: center;
    font-weight: 700;
  }
  .website {
    top: 428px;
    font-size: 30px;
  }
  .email {
    top: 474px;
    font-size: 22px;
    font-weight: 400;
  }
</style>
</head>
<body>
  <div class="card">
    <svg class="card-frame" width="1040" height="594" viewBox="0 0 1040 594" aria-hidden="true">
      <rect x="45" y="45" width="950" height="504" rx="24" fill="none" stroke="var(--ink)" stroke-width="4"/>
      <g fill="var(--ink)">
        <path d="M560 64 l8 8 -8 8 -8 -8z M620 64 l8 8 -8 8 -8 -8z M680 64 l8 8 -8 8 -8 -8z M740 64 l8 8 -8 8 -8 -8z M800 64 l8 8 -8 8 -8 -8z M860 64 l8 8 -8 8 -8 -8z"/>
        <path d="M180 520 l8 8 -8 8 -8 -8z M240 520 l8 8 -8 8 -8 -8z M300 520 l8 8 -8 8 -8 -8z M360 520 l8 8 -8 8 -8 -8z M420 520 l8 8 -8 8 -8 -8z M480 520 l8 8 -8 8 -8 -8z"/>
      </g>
    </svg>

    <div class="postmark" role="img" aria-label="Cachet postal vintage estompé"></div>

    <div class="brand-seal">
      <p class="brand-name">La Table de Rive Bleue</p>
    </div>

    <p class="reminder"><span class="initial">N</span>'oubliez pas<br>que nous sommes<br>ici si vous avez<br>besoin de nous</p>

    <p class="contact website">www.latablederivebleue.com</p>
    <p class="contact email">nouscontact@latablederivebleue.com</p>
  </div>
</body>
</html>
```